Rock Concert Ticket

Invitation for a 50th birthday party in the form of a ticket to a rock concert -
think Boots 'n Ravens, QX/TB, Velvet Harpoons, The Tundra, Tin Marmot etc.
Design should be very rock n roll with album cover type feel. Needs to reference 50 and include information like venue, date, dress code, rsvp etc. Invitation to be distributed electronically rather than hard copy.

Reason: Deadline has been extended to allow for some slight changes to 2-3 of the designs that I have narrowed it down to. I contacted the designers directly with feedback so you know who you are. Thanks

```html
<!DOCTYPE html>
<html lang="en">
<head>
<meta charset="utf-8">
<title>It's only r'n'r — 50th Birthday Ticket</title>
<link rel="stylesheet" href="https://fonts.googleapis.com/css2?family=Share+Tech+Mono&display=swap">
<style>
  :root {
    --backdrop: #3f3e40;
    --base-strip: #ffffff;
    --ink: #1c1a1a;
    --paper-white: #ffffff;
    --flame-red: #d4242a;
    --flame-orange: #ee7424;
    --sun-yellow: #f6c41b;
    --pale-grey: #d9d6d4;
    --stone-grey: #a8a7a3;
    --slate-teal: #5f7a82;
    --title-red: #c9462b;
    --title-olive: #c9b52a;
    --title-green: #7fa43a;
  }
  * { box-sizing: border-box; margin: 0; padding: 0; }
  html, body {
    width: 1200px;
    height: 905px;
    overflow: hidden;
    background: var(--backdrop);
  }
  .stage {
    position: relative;
    width: 1200px;
    height: 905px;
    background: var(--backdrop);
  }
  .stage__base {
    position: absolute;
    left: 0; right: 0; bottom: 0;
    height: 36px;
    background: var(--base-strip);
  }
  .ticket {
    position: absolute;
    left: 278px;
    top: 242px;
    width: 647px;
    height: 240px;
    overflow: hidden;
    box-shadow: 0 6px 10px rgba(0, 0, 0, 0.45);
    font-family: "Share Tech Mono", monospace;
  }
  .ticket__art {
    position: absolute;
    inset: 0 187px 0 0;
    background:
      linear-gradient(160deg, rgba(33, 150, 140, 0.0) 40%, rgba(33, 150, 140, 0.55) 48%, rgba(33, 60, 80, 0.6) 54%, rgba(33, 150, 140, 0) 62%),
      linear-gradient(180deg, var(--sun-yellow) 0%, #f4a21e 55%, var(--flame-orange) 100%);
  }
  .ticket__art::before {
    content: "";
    position: absolute;
    left: 0; top: 0; bottom: 0;
    width: 50px;
    background: linear-gradient(180deg, var(--flame-orange) 0%, var(--flame-red) 60%, var(--slate-teal) 100%);
  }
  .ticket__edge {
    position: absolute;
    top: 0; right: 0; bottom: 0;
    width: 66px;
    background: linear-gradient(180deg, var(--flame-red) 0%, var(--flame-orange) 45%, var(--flame-red) 75%, var(--slate-teal) 100%);
  }
  .title {
    position: absolute;
    top: 25px;
    left: 0;
    display: flex;
    gap: 0;
  }
  .title__word {
    position: absolute;
    top: 0;
    height: 52px;
    background: var(--ink);
    font-size: 44px;
    line-height: 52px;
    padding: 0 8px;
    white-space: nowrap;
  }
  .title__word--its { left: 0; width: 111px; color: var(--title-red); }
  .title__word--only { left: 140px; width: 112px; color: var(--title-olive); }
  .title__word--rnr { left: 261px; width: 159px; color: var(--title-green); }
  .details {
    position: absolute;
    left: 9px;
    top: 98px;
    color: var(--paper-white);
    font-size: 26px;
    line-height: 24px;
    list-style: none;
    letter-spacing: 0.5px;
  }
  .stub {
    position: absolute;
    top: 0;
    left: 460px;
    width: 121px;
    height: 240px;
  }
  .stub__icon {
    position: absolute;
    left: 0; top: 0;
    width: 121px;
    height: 108px;
    background: linear-gradient(180deg, var(--pale-grey) 0%, #b9b6b4 100%);
  }
  .stub__icon::after {
    content: "";
    position: absolute;
    left: 42px; top: 18px;
    width: 34px; height: 70px;
    background: var(--ink);
    border-radius: 10px;
  }
  .stub__number {
    position: absolute;
    left: 0; top: 108px;
    width: 121px;
    height: 132px;
    background: var(--ink);
    overflow: hidden;
  }
  .stub__digits {
    position: absolute;
    left: 50%;
    top: 50%;
    transform: translate(-50%, -50%) rotate(90deg);
    color: var(--stone-grey);
    font-size: 104px;
    line-height: 1;
  }
</style>
</head>
<body>
  <main class="stage">
    <article class="ticket">
      <div class="ticket__art" role="img" aria-label="Abstract poster artwork: orange, yellow and red angular shapes crossed by a teal brush stroke"></div>
      <div class="ticket__edge"></div>

      <h1 class="title">
        <span class="title__word title__word--its">It’s</span>
        <span class="title__word title__word--only">only</span>
        <span class="title__word title__word--rnr">r’n’r</span>
      </h1>

      <ul class="details">
        <li>date 13,sep 2014</li>
        <li>dress code xxxx</li>
        <li>xxxx xxxx</li>
        <li>xxxx xxxx</li>
      </ul>

      <aside class="stub">
        <div class="stub__icon" role="img" aria-label="Illustration of a hand with crossed fingers"></div>
        <div class="stub__number"><span class="stub__digits">50</span></div>
      </aside>
    </article>
    <div class="stage__base"></div>
  </main>
</body>
</html>
```